Landing Page Design for Adult Dating Age Verification (18+)

The objective of this task is to design a visually appealing pre-landing page for the adult dating site "Plumvelle (site: https://plumvelle.example/)" with an age verification mechanism. The pre-landing page will feature two buttons that redirect visitors to the main offer. The design should also include a footer block that includes links to the terms of use, privacy policy, and contact us pages.

Design Requirements:
Develop an age verification section prominently displayed on the pre-landing page.
Design the section to include two buttons labeled "Yes" and "No" for visitors to confirm their age.
Ensure the section is visually appealing and clearly communicates the purpose of age verification.

Visual Appeal:
Create a visually appealing design that aligns with the branding and theme of the "Plumvelle" adult dating site.
Use suitable color schemes, typography, and graphics to enhance the overall visual appeal of the pre-landing page.

Layout and Navigation:
Design an engaging and intuitive layout that encourages visitors to interact with the page and proceed to the main offer.
Ensure clear and visible navigation elements that direct visitors to the main offer or provide additional information.

Responsive Design:
Develop a responsive design that provides a seamless user experience across various devices, including desktop and mobile.
Ensure the design elements and layout adapt well to different screen sizes and resolutions.

File Formats and Assets:
Deliver the final design in PSD, AI, or Sketch format, ensuring that the files are well-organized and layered.
Include any necessary images or assets used in the design, ensuring they are of high quality and optimized for web use.

```html
<!DOCTYPE html>
<html lang="en">
<head>
<meta charset="utf-8">
<title>Plumvelle — Age Verification</title>
<link href="https://fonts.googleapis.com/css2?family=Cagliostro&family=Montserrat:wght@500;600&display=swap" rel="stylesheet">
<style>
  :root {
    --bg-pink: #f68b9f;
    --bg-glow: #fbe6ec;
    --plum: #86083a;
    --plum-soft: #8c1a45;
    --button: #a83c5d;
    --button-text: #ffffff;
    --figure-light: #f9b8c8;
    --checkbox-border: #a8204f;
  }
  * { margin: 0; padding: 0; box-sizing: border-box; }
  html, body { width: 1200px; height: 547px; overflow: hidden; }
  body { font-family: "Cagliostro", sans-serif; color: var(--plum); }

  .landing {
    position: relative;
    width: 1200px;
    height: 547px;
    overflow: hidden;
    background:
      radial-gradient(ellipse 260px 320px at 850px 170px, var(--bg-glow) 0%, rgba(251,230,236,0.55) 35%, rgba(246,139,159,0) 100%),
      linear-gradient(90deg, #f795a8 0%, #f7a1b2 45%, var(--bg-pink) 100%);
  }

  .brand {
    position: absolute;
    left: 176px;
    top: 98px;
    display: flex;
    align-items: center;
    gap: 12px;
  }
  .brand-dot {
    width: 56px;
    height: 56px;
    border-radius: 50%;
    background: var(--plum);
  }
  .brand-name {
    font-size: 40px;
    line-height: 1;
    color: var(--plum);
  }

  .headline {
    position: absolute;
    left: 175px;
    top: 224px;
    font-size: 48px;
    font-weight: 400;
    line-height: 1.1;
    color: var(--plum);
    -webkit-text-stroke: 0.6px var(--plum);
  }
  .intro {
    position: absolute;
    left: 177px;
    top: 285px;
    width: 370px;
    font-size: 17px;
    line-height: 27px;
    color: var(--plum-soft);
    -webkit-text-stroke: 0.3px var(--plum-soft);
  }
  .age-question {
    position: absolute;
    left: 177px;
    top: 358px;
    font-family: "Montserrat", sans-serif;
    font-weight: 500;
    font-size: 16px;
    color: var(--plum-soft);
  }
  .age-actions {
    position: absolute;
    left: 177px;
    top: 387px;
    display: flex;
    gap: 10px;
  }
  .age-button {
    width: 54px;
    height: 42px;
    display: flex;
    align-items: center;
    justify-content: center;
    background: var(--button);
    color: var(--button-text);
    font-family: "Montserrat", sans-serif;
    font-weight: 600;
    font-size: 16px;
    text-decoration: none;
  }
  .remember {
    position: absolute;
    left: 177px;
    top: 442px;
    display: flex;
    align-items: center;
    gap: 7px;
    font-family: "Montserrat", sans-serif;
    font-weight: 500;
    font-size: 12px;
    color: var(--plum-soft);
  }
  .remember-box {
    width: 13px;
    height: 13px;
    border: 1px solid var(--checkbox-border);
    background: #f4eef0;
  }

  .site-footer {
    position: absolute;
    left: 177px;
    top: 514px;
    display: flex;
    gap: 18px;
    font-family: "Montserrat", sans-serif;
    font-weight: 500;
    font-size: 11px;
  }
  .site-footer a { color: var(--plum-soft); text-decoration: none; }

  .couple-illustration {
    position: absolute;
    left: 660px;
    top: 40px;
    width: 340px;
    height: 540px;
    border-radius: 50% 55% 35% 40% / 22% 30% 10% 12%;
    background: radial-gradient(ellipse 70% 60% at 50% 45%, #86083a 0%, #8a1040 55%, rgba(140,20,68,0.85) 80%, rgba(246,139,159,0) 100%);
    filter: blur(3px);
  }
  .figure-illustration {
    position: absolute;
    left: 8px;
    top: 335px;
    width: 195px;
    height: 200px;
    border-radius: 45% 55% 30% 40% / 40% 45% 25% 30%;
    background: radial-gradient(ellipse at 45% 45%, var(--figure-light) 0%, rgba(249,184,200,0.7) 60%, rgba(247,166,187,0) 100%);
    filter: blur(2px);
  }
</style>
</head>
<body>
  <main class="landing">
    <div class="figure-illustration" role="img" aria-label="Light pink silhouette of a crouching woman in heels"></div>
    <div class="couple-illustration" role="img" aria-label="Dark plum silhouette of a couple embracing and kissing"></div>

    <div class="brand">
      <span class="brand-dot"></span>
      <span class="brand-name">Plumvelle</span>
    </div>

    <h1 class="headline">Find Your Match</h1>
    <p class="intro">Welcome to Our Dating Site.The Place Where Your can Find What Your Heart Desires!</p>

    <p class="age-question">Are You Over 18 years of Age?</p>
    <div class="age-actions">
      <a class="age-button" href="https://plumvelle.example/">Yes</a>
      <a class="age-button" href="https://plumvelle.example/">No</a>
    </div>
    <label class="remember"><span class="remember-box"></span>Remember Me</label>

    <footer class="site-footer">
      <a href="https://plumvelle.example/terms">Terms of Use</a>
      <a href="https://plumvelle.example/privacy">Privacy Policy</a>
      <a href="https://plumvelle.example/contact">Contact Us</a>
    </footer>
  </main>
</body>
</html>
```